indoor tennis and sports center( club)

we need a logo for a new business venture, it will be for business cards and for presentations.
presentations for potential investors and authorities.
the design needs to communicate the sport and a community of tennis players
the center includes a tennis academy, and sports club with training sessions for all ages

Reason: so that I can get some more feedback on my side as to te design we want

Target Market(s)

potential investors or partners

Industry/Entity Type

Business

Contact Information for Business Card

i need the name of the club
names of the partners
slogan" changing lives through tennis" on the front
the clubs three main goals are ports education , academy and a community club

Colors
3176b5
33b8a4
fbee3d
0dac94
acd036

Requirements
Must have
• a strong logo
• names of the partners
• web site and email address
• tel number
Nice to have
• a connection between the different aspects of the club

```html
<!DOCTYPE html>
<html lang="en">
<head>
<meta charset="utf-8">
<title>Baseline Hall – Business Card</title>
<link href="https://fonts.googleapis.com/css2?family=Roboto:wght@300;400;500&family=Kalam:wght@400&display=swap" rel="stylesheet">
<style>
  :root {
    --page-bg: #e9e8e4;
    --card-white: #fbfbfb;
    --card-white-shade: #ececec;
    --brand-green: #6cae4e;
    --green-light: #8cc76a;
    --green-deep: #5a9a3f;
    --ink-dark: #3c3f41;
    --ink-mid: #4a4d4f;
    --figure-grey: #dcdcdc;
  }
  * { box-sizing: border-box; margin: 0; padding: 0; }
  html, body {
    width: 1200px; height: 1023px; overflow: hidden;
    background: var(--page-bg);
    font-family: "Roboto", sans-serif;
  }
  .canvas {
    width: 1200px; height: 1023px;
    display: flex; flex-direction: column; align-items: center; justify-content: center;
    gap: 40px;
  }
  .card {
    position: relative;
    width: 760px; height: 434px;
    border-radius: 22px;
    overflow: hidden;
    box-shadow: 0 6px 18px rgba(0,0,0,0.12);
  }

  /* Front */
  .card--front {
    background: linear-gradient(160deg, var(--card-white) 40%, var(--card-white-shade) 100%);
  }
  .card--front .edge-band {
    position: absolute; left: 0; right: 0; bottom: 0; height: 22px;
    background: var(--brand-green);
  }
  .player-figure {
    position: absolute; right: 60px; top: 20px;
    width: 250px; height: 392px;
    border-radius: 120px 120px 20px 20px;
    background: linear-gradient(180deg, rgba(200,200,200,0.45), rgba(220,220,220,0.15));
  }
  .brand {
    position: absolute; left: 48px; top: 120px;
    display: flex; align-items: center; gap: 16px;
  }
  .brand__mark {
    width: 80px; height: 80px; border-radius: 50%;
    background: var(--brand-green);
    flex-shrink: 0;
  }
  .brand__name {
    font-family: "Kalam", cursive;
    font-size: 64px; line-height: 1;
    color: var(--brand-green);
    padding-top: 10px;
  }
  .person {
    position: absolute; left: 150px; top: 238px;
  }
  .person__name { font-size: 30px; font-weight: 400; color: var(--ink-dark); line-height: 1.05; }
  .person__title { font-size: 17px; color: var(--brand-green); letter-spacing: 0.5px; }
  .contact {
    position: absolute; left: 150px; top: 310px;
    list-style: none;
  }
  .contact li {
    display: flex; align-items: center; gap: 10px;
    font-size: 17px; font-weight: 300; color: var(--ink-mid);
    letter-spacing: 0.8px; line-height: 28px;
  }
  .contact svg { width: 16px; height: 16px; flex-shrink: 0; }
  .pillars {
    position: absolute; right: 48px; top: 48px;
    list-style: none; text-align: right;
  }
  .pillars li {
    font-size: 19px; font-weight: 400; color: var(--ink-mid);
    letter-spacing: 1.2px; line-height: 30px;
  }
  .pillars li::after {
    content: ""; display: inline-block;
    width: 6px; height: 6px; border-radius: 50%;
    background: var(--brand-green);
    margin-left: 8px; vertical-align: middle;
  }

  /* Back */
  .card--back {
    background: radial-gradient(circle at 60% 35%, var(--green-light) 0%, var(--brand-green) 55%, var(--green-deep) 100%);
  }
  .back-brand {
    position: absolute; left: 0; right: 0; top: 110px;
    display: flex; align-items: center; justify-content: center; gap: 18px;
  }
  .back-brand .brand__mark {
    width: 110px; height: 110px; background: #f4f6f2;
  }
  .back-brand .brand__name {
    font-size: 84px; color: var(--ink-dark);
  }
  .slogan {
    position: absolute; left: 0; right: 0; top: 292px;
    text-align: center;
    font-size: 24px; font-weight: 400; color: #ffffff;
    letter-spacing: 4px;
  }
</style>
</head>
<body>
<main class="canvas">

  <section class="card card--front" aria-label="Business card front">
    <div class="player-figure" role="img" aria-label="Faint silhouette of a tennis player raising a racket"></div>

    <div class="brand">
      <span class="brand__mark"></span>
      <span class="brand__name">Baseline Hall</span>
    </div>

    <div class="person">
      <p class="person__name">Your Name</p>
      <p class="person__title">Title</p>
    </div>

    <ul class="contact">
      <li>
        <svg viewBox="0 0 16 16" aria-hidden="true"><circle cx="8" cy="8" r="7" fill="none" stroke="#6cae4e" stroke-width="1.4"/><path d="M5.5 4.5l1.5 0 0.7 2-1 0.8a5 5 0 0 0 2 2l0.8-1 2 0.7 0 1.5c-3.5 0.5-6.5-2.5-6-6z" fill="#6cae4e"/></svg>
        55-010-24680
      </li>
      <li>
        <svg viewBox="0 0 16 16" aria-hidden="true"><rect x="1.5" y="3.5" width="13" height="9" fill="none" stroke="#6cae4e" stroke-width="1.4"/><path d="M1.5 3.5l6.5 5 6.5-5M1.5 12.5l5-4.5M14.5 12.5l-5-4.5" fill="none" stroke="#6cae4e" stroke-width="1.2"/></svg>
        info@baselinehall.net
      </li>
      <li>
        <svg viewBox="0 0 16 16" aria-hidden="true"><circle cx="8" cy="8" r="6.5" fill="none" stroke="#6cae4e" stroke-width="1.3"/><ellipse cx="8" cy="8" rx="3" ry="6.5" fill="none" stroke="#6cae4e" stroke-width="1.1"/><path d="M1.5 8h13M2.5 5h11M2.5 11h11" stroke="#6cae4e" stroke-width="1"/></svg>
        www.baselinehall.net
      </li>
    </ul>

    <ul class="pillars">
      <li>Indoor club</li>
      <li>Academy</li>
      <li>Education</li>
    </ul>

    <div class="edge-band"></div>
  </section>

  <section class="card card--back" aria-label="Business card back">
    <div class="back-brand">
      <span class="brand__mark"></span>
      <span class="brand__name">Baseline Hall</span>
    </div>
    <p class="slogan">Changing lives through Tennis</p>
  </section>

</main>
</body>
</html>
```